BBQ Catering & Pop-up Restaurant

I'm a catering company and a pop-up restaurant and need a website that will have the following at minimum (I'm open to suggestions): about me section, menu section, events section, a pre-order page. Here is an example of a site that I really like ... https://hollowpitsmoke.example/ . I want to have a pre-order page where people can place orders online and the ability to take credit card payments. I've included a word doc with a draft write up to get started.
Updates

Project Deadline Extended
Reason: I am awaiting feedback from my partner and will be in touch ASAP.

Target Market(s)

BBQ Lovers

Industry/Entity Type

Caterer

Font styles to use
Serif
Other font styles liked:
• we can use multiple fonts where appropriate. I also like a faded, woody type font - which reminds me of the old western movies

Colors

Designer to choose colors to be used in the design.

Requirements
Must have
• I want
• - a smokey, woody, bbq type feel to the site.
• - my logo to be utilized
• - colors I like should compliment the colors in my logo
• - link to sign up for a news letter/ mailing list and something on the back end to capture data
Nice to have
• NA
Should not have
• NA

```html
<!DOCTYPE html>
<html lang="en">
<head>
<meta charset="utf-8">
<title>Emberline Smokehouse BBQ</title>
<link href="https://fonts.googleapis.com/css2?family=Roboto+Slab:wght@400;700&family=Lato:wght@400;700&display=swap" rel="stylesheet">
<style>
:root{
  --red:#a8281d;
  --red-dark:#7e1a12;
  --yellow:#f2c12e;
  --ink:#1d1714;
  --char:#231c18;
  --wood-1:#5a3420;
  --wood-2:#7a4a2c;
  --wood-3:#3e2414;
  --cream:#f3ead9;
  --white:#ffffff;
  --muted:#cfc4b6;
  --gold-line:#b8862e;
}
*{box-sizing:border-box;margin:0;padding:0}
html,body{width:1200px;height:3136px;overflow:hidden}
body{position:relative;background:var(--char);font-family:"Lato",Arial,sans-serif;color:var(--white)}
.abs{position:absolute}
h2,h3,.slab{font-family:"Roboto Slab",Georgia,serif}

.divider{position:absolute;height:14px}
.divider::before{content:"";position:absolute;left:0;right:0;top:6px;height:2px;background:var(--gold-line);opacity:.8}
.divider::after{content:"";position:absolute;left:50%;top:1px;width:12px;height:12px;margin-left:-6px;background:var(--gold-line);transform:rotate(45deg)}

.hero{left:0;top:0;width:1200px;height:570px;background:linear-gradient(180deg,#3a2a22 0%,#7d5330 35%,#b0612e 55%,#6a2a1e 80%,#2c1d18 100%)}
.topbar{left:0;top:0;width:1200px;height:100px;background:linear-gradient(180deg,rgba(20,12,8,.75),rgba(20,12,8,0))}
.call{left:163px;top:14px;font-size:15px;display:flex;align-items:center;gap:10px}
.call .ring{width:28px;height:28px;border:1px solid rgba(255,255,255,.6);border-radius:50%;display:flex;align-items:center;justify-content:center}
.reserve{left:874px;top:11px;width:163px;height:32px;background:var(--red);font:700 12px "Roboto Slab",serif;letter-spacing:.5px;display:flex;align-items:center;justify-content:center}
.nav a{position:absolute;top:63px;font:700 12px "Roboto Slab",serif;color:var(--white);text-decoration:none;text-transform:uppercase}
.nav a.active{color:var(--yellow)}
.nav .line{position:absolute;left:163px;top:86px;width:874px;height:1px;background:rgba(255,255,255,.35)}
.nav .active-line{position:absolute;left:163px;top:85px;width:40px;height:3px;background:var(--yellow)}
.brand{left:510px;top:24px;width:180px;height:80px;display:flex;align-items:center;justify-content:center;text-align:center;font:700 20px/1.1 "Roboto Slab",serif;color:var(--white)}
.hero-arrow{top:330px}
.hero-caption{right:163px;top:412px;text-align:right}
.hero-caption h1{font:700 26px "Roboto Slab",serif;letter-spacing:.5px;text-transform:uppercase}
.hero-caption p{font-size:14px;line-height:20px;margin-top:8px;width:370px;margin-left:auto}

.about{left:0;top:570px;width:1200px;height:315px;background:var(--red)}
.about h2{position:absolute;left:163px;top:36px;font-size:23px}
.about .divider{left:163px;top:84px;width:380px}
.about p{position:absolute;left:163px;top:120px;width:540px;font-size:12.5px;line-height:24px;color:#f6e3df}
.chef{left:722px;top:523px;width:316px;height:316px;border-radius:50%;background:var(--white);padding:8px}
.chef .photo{width:100%;height:100%;border-radius:50%;background:radial-gradient(circle at 50% 40%,#fafafa 0%,#d9d4cf 45%,#7b6e66 100%)}
.read-more{left:729px;top:756px;width:84px;height:84px;border-radius:50%;background:var(--yellow);color:var(--ink);font:700 11px/1.2 "Roboto Slab",serif;display:flex;flex-direction:column;align-items:center;justify-content:center;text-align:center}

.wood{background:linear-gradient(90deg,var(--wood-3) 0%,var(--wood-2) 25%,var(--wood-1) 50%,var(--wood-2) 75%,var(--wood-3) 100%)}
.menu{left:0;top:885px;width:1200px;height:1122px}
.sec-title{position:absolute;left:0;width:1200px;text-align:center;font:700 24px "Roboto Slab",serif;text-transform:uppercase}
.card{position:absolute;top:1020px;width:276px;height:418px;background:var(--white);color:var(--ink);padding:8px;box-shadow:0 6px 14px rgba(0,0,0,.45)}
.card .food{width:260px;height:205px}
.card h3{font-size:14px;margin:22px 0 0 8px;text-transform:uppercase}
.card .rule{width:60px;height:2px;background:var(--red);margin:8px 0 0 8px}
.card p{font-size:12.5px;line-height:18px;margin:14px 8px 0}
.card .price{font:700 19px "Roboto Slab",serif;color:var(--red);margin:12px 0 0 8px}
.order-btn{position:absolute;top:1416px;width:110px;height:36px;background:var(--yellow);color:var(--ink);font:700 11px "Roboto Slab",serif;display:flex;align-items:center;justify-content:center;text-transform:uppercase}
.how-circle{position:absolute;top:1616px;width:188px;height:188px;border-radius:50%;background:#1a1310;display:flex;align-items:center;justify-content:center}
.how-circle .inner{width:150px;height:150px;border-radius:50%;border:6px solid var(--white);display:flex;align-items:center;justify-content:center}
.option{position:absolute;top:1838px;width:150px;height:44px;border:2px solid var(--white);border-radius:4px;background:rgba(0,0,0,.25);font:700 20px "Roboto Slab",serif;display:flex;align-items:center;justify-content:center}
.how-text{position:absolute;top:1902px;width:400px;text-align:center;font-size:13px;line-height:22px}
.how-text b{color:var(--yellow);font-weight:400}
.vdots{left:599px;top:1620px;height:330px;border-left:2px dotted rgba(255,255,255,.4)}

.news{left:0;top:2007px;width:1200px;height:303px;background:linear-gradient(90deg,#14100d,#2b1f18 50%,#14100d)}
.news h2{position:absolute;top:42px;font-size:23px;text-transform:uppercase}
.news .blurb{left:163px;top:123px;width:420px;font-size:12px;line-height:20px;color:var(--muted)}
.email{left:163px;top:175px;width:318px;height:32px;background:var(--white);color:#888;font-size:12px;padding:0 12px;display:flex;align-items:center}
.subscribe{left:163px;top:230px;width:94px;height:34px;background:var(--yellow);color:var(--ink);font:700 11px "Roboto Slab",serif;display:flex;align-items:center;justify-content:center;text-transform:uppercase}
.social{position:absolute;top:128px;display:flex;align-items:center;gap:12px}
.social .name{font:700 17px "Roboto Slab",serif;text-transform:uppercase}
.social .tag{display:inline-block;margin-top:4px;background:#3a6fb4;font-size:10px;font-weight:700;padding:2px 10px}

.events{left:0;top:2310px;width:1200px;height:512px}
.calendar{left:163px;top:2452px;width:349px;height:311px;background:#2a1d16;border:1px solid #5e4332}
.cal-head{height:30px;background:var(--red);display:flex;align-items:center;justify-content:space-between;padding:0 10px;font:700 14px "Roboto Slab",serif}
.cal-head span.arrow{width:20px;height:20px;border-radius:50%;background:var(--white);color:var(--red);font-size:12px;display:flex;align-items:center;justify-content:center}
.cal-days{display:grid;grid-template-columns:repeat(7,1fr);background:#e8e2da;color:#444;font-size:8px;height:16px;align-items:center;text-align:center}
.cal-grid{display:grid;grid-template-columns:repeat(7,1fr);grid-auto-rows:43px;gap:0;padding:4px}
.cal-grid div{display:flex;align-items:center;justify-content:center;font-size:9px;color:#ddd;border:1px solid #3d2b21;margin:2px}
.cal-grid div.hl{background:var(--yellow);color:var(--ink);border-color:var(--yellow)}
.cal-grid div.sel{background:var(--red);color:var(--white);border-color:var(--red)}
.event{position:absolute;border:4px solid rgba(255,255,255,.18)}
.event .pic{width:100%;height:100%}
.event .cap{position:absolute;left:0;right:0;bottom:0;height:44px;background:rgba(20,14,10,.82);display:flex;align-items:center;font-size:11px;line-height:14px}
.event .date{width:40px;flex:none;text-align:center;border-right:1px solid rgba(255,255,255,.3);margin-right:10px;font:700 12px/1.2 "Roboto Slab",serif}
.event .date small{display:block;font:400 10px "Lato",sans-serif}

.footer{left:0;top:2822px;width:1200px;height:314px;background:#171210}
.footer .edge{position:absolute;left:0;top:-8px}
.footer h4{position:absolute;top:48px;font:700 14px "Roboto Slab",serif;text-transform:uppercase}
.footer .u{position:absolute;top:72px;height:1px;background:rgba(255,255,255,.25)}
.links{left:163px;top:92px;list-style:none;font-size:12px;line-height:25px}
.links li::before{content:"\2022";color:var(--yellow);margin-right:10px}
.contact{left:351px;top:92px;font-size:12px;line-height:17px;width:230px}
.contact strong{display:block;font-size:13px;margin-bottom:2px}
.contact .row{display:flex;align-items:center;gap:8px;margin-top:14px;white-space:nowrap}
.map{left:610px;top:94px;width:196px;height:134px;background:linear-gradient(135deg,#dfe7d6,#c7d6e3 55%,#e6dfcf)}
.foot-brand{left:868px;top:104px;width:160px;height:110px;display:flex;align-items:center;justify-content:center;text-align:center;font:700 20px/1.15 "Roboto Slab",serif;color:var(--white)}
.copy-line{left:163px;top:268px;width:874px;height:1px;background:rgba(255,255,255,.2)}
.copy{left:163px;top:282px;font-size:11px;color:var(--muted)}
.pay{left:826px;top:278px;display:flex;gap:8px}
.pay span{width:36px;height:22px;background:#e9e6e1;border-radius:3px}
</style>
</head>
<body>

<section class="abs hero" role="img" aria-label="Evening photograph of a busy outdoor restaurant terrace with red umbrellas"></section>
<div class="abs topbar"></div>
<div class="abs call">
  <span class="ring"><svg width="14" height="14" viewBox="0 0 24 24"><path fill="#fff" d="M6.6 10.8a15 15 0 0 0 6.6 6.6l2.2-2.2c.3-.3.7-.4 1-.2 1.1.4 2.3.6 3.6.6.6 0 1 .4 1 1V20c0 .6-.4 1-1 1C10.6 21 3 13.4 3 4c0-.6.4-1 1-1h3.5c.6 0 1 .4 1 1 0 1.3.2 2.5.6 3.6.1.3 0 .7-.2 1z"/></svg></span>
  Please Don't Hesitate To Call : (555) 014-2290
</div>
<div class="abs reserve">MAKE A RESERVATION</div>
<nav class="nav">
  <a class="active" style="left:163px">Home</a>
  <a style="left:272px">About Us</a>
  <a style="left:405px">Menu</a>
  <a style="left:752px">Pre-Order</a>
  <a style="left:869px">Events</a>
  <a style="left:964px">Contact Us</a>
  <span class="line"></span><span class="active-line"></span>
</nav>
<div class="abs brand">Emberline Smokehouse BBQ</div>
<svg class="abs hero-arrow" style="left:62px" width="24" height="40" viewBox="0 0 24 40"><path d="M20 4 4 20l16 16" stroke="#fff" stroke-width="3" fill="none"/></svg>
<svg class="abs hero-arrow" style="left:1114px" width="24" height="40" viewBox="0 0 24 40"><path d="m4 4 16 16L4 36" stroke="#fff" stroke-width="3" fill="none"/></svg>
<div class="abs hero-caption">
  <h1>Duis Aute Reprehenderit</h1>
  <p>Ut enim ad minim veniam, quis nostrud exercitation ullamco laboris nisi ut aliquip ex ea commodo consequat</p>
</div>

<section class="abs about">
  <h2>WHO ARE WE?</h2>
  <div class="divider"></div>
  <p>Until recently, I've been a guy that sells smoked ribs to family and friends on the weekends. We're talking <b>ONE-MAN-SHOW</b> – it's been a lot of fun, but super exhausting. Alhamdulillah, I've received overwhelmingly positive feedback on the ribs and I've been receiving a lot of new order requests from folks as well as a lot of repeat customers (this is always a good sign). So nooow, I'm a guy that sells ribs on the weekends to family and friends...and friends of family... and friends of friends – so basically nothing has changed....but they're about to</p>
</section>
<div class="abs chef"><div class="photo" role="img" aria-label="Portrait photograph of the pitmaster in chef whites"></div></div>
<div class="abs read-more">READ MORE<span>&raquo;</span></div>

<section class="abs menu wood"></section>
<h2 class="sec-title" style="top:925px">Menu &amp; Pricing</h2>
<div class="divider" style="left:430px;top:972px;width:340px"></div>
<svg class="abs" style="left:104px;top:1214px" width="20" height="34" viewBox="0 0 20 34"><path d="M17 2 3 17l14 15" stroke="#fff" stroke-width="2" fill="none"/></svg>
<svg class="abs" style="left:1076px;top:1214px" width="20" height="34" viewBox="0 0 20 34"><path d="m3 2 14 15L3 32" stroke="#fff" stroke-width="2" fill="none"/></svg>

<article class="card" style="left:163px">
  <div class="food" role="img" aria-label="Photograph of smoked beef short ribs on a plate" style="background:radial-gradient(circle at 50% 55%,#6b2a1a,#3a1a10 60%,#e8e2dc 100%)"></div>
  <h3>Beef Short Ribs</h3><div class="rule"></div>
  <p>Duis aute irure dolor in reprehenderit in voluptate velit esse cillum dolore eu fugiat nulla pariatur. Excepteur sint</p>
  <div class="price">$20/lb</div>
</article>
<article class="card" style="left:462px">
  <div class="food" role="img" aria-label="Photograph of smoked beef back ribs" style="background:radial-gradient(circle at 50% 50%,#4a2518,#2a1610 60%,#8a7464 100%)"></div>
  <h3>Beef Back Ribs</h3><div class="rule"></div>
  <p>Duis aute irure dolor in reprehenderit in voluptate velit esse cillum dolore eu fugiat nulla pariatur. Excepteur sint</p>
  <div class="price">$18/lb</div>
</article>
<article class="card" style="left:761px">
  <div class="food" role="img" aria-label="Photograph of sliced smoked beef brisket with vegetables" style="background:radial-gradient(circle at 55% 55%,#8a3a2a,#5a2a1c 50%,#d9cfc4 100%)"></div>
  <h3>Beef Brisket</h3><div class="rule"></div>
  <p>Duis aute irure dolor in reprehenderit in voluptate velit esse cillum dolore eu fugiat nulla pariatur. Excepteur sint</p>
  <div class="price">$22/lb</div>
</article>
<div class="order-btn" style="left:176px">Order Now</div>
<div class="order-btn" style="left:475px">Order Now</div>
<div class="order-btn" style="left:774px">Order Now</div>

<h2 class="sec-title" style="top:1533px">How Can You Order From Us?</h2>
<div class="divider" style="left:310px;top:1581px;width:580px"></div>
<div class="abs vdots"></div>
<div class="how-circle" style="left:251px"><div class="inner">
  <svg width="70" height="70" viewBox="0 0 70 70" fill="none" stroke="#fff" stroke-width="3"><rect x="12" y="8" width="38" height="50" rx="3"/><path d="M20 20h4M30 20h14M20 30h4M30 30h14M20 40h4M30 40h10"/><path d="M46 42v-6a4 4 0 0 1 8 0v16c0 6-4 10-10 10h-2"/></svg>
</div></div>
<div class="how-circle" style="left:751px"><div class="inner">
  <svg width="70" height="70" viewBox="0 0 70 70" fill="none" stroke="#fff" stroke-width="3"><circle cx="20" cy="35" r="8"/><circle cx="50" cy="16" r="8"/><circle cx="50" cy="54" r="8"/><path d="M27 31l16-11M27 39l16 11"/></svg>
</div></div>
<div class="option" style="left:261px">Option 1</div>
<div class="option" style="left:770px">Option 2</div>
<p class="how-text" style="left:145px">We have a minimum party requirement of 5 lbs. on meat orders with at least 48 hour advance notice, the sooner the better, this will allow us to ensure we have ribs ... <b>[+]</b></p>
<p class="how-text" style="left:640px">We'll periodically announce "smoke sessions" via social media &amp; email where you can place an order for a particular weekend. For example, we may ... <b>[+]</b></p>

<section class="abs news">
  <h2 style="left:163px">Newsletter Signup</h2>
  <div class="divider" style="left:163px;top:88px;width:418px"></div>
  <h2 style="left:617px">Follow</h2>
  <div class="divider" style="left:617px;top:88px;width:420px"></div>
  <p class="abs blurb">Sign up to receive occasional e-mail updates about new features and special offers from <b style="color:#fff">Emberline Smokehouse BBQ</b></p>
  <div class="abs email">Enter Your Email Here</div>
  <div class="abs subscribe">Subscribe</div>
  <div class="social" style="left:617px">
    <svg width="90" height="78" viewBox="0 0 90 78"><path d="M23 2h44l21 37-21 37H23L2 39z" fill="none" stroke="#ddd" stroke-width="2"/><circle cx="45" cy="39" r="14" fill="#3a6fb4"/></svg>
    <div><div class="name">Smokebook</div><span class="tag">LIKE</span></div>
  </div>
  <div class="social" style="left:830px">
    <svg width="90" height="78" viewBox="0 0 90 78"><path d="M23 2h44l21 37-21 37H23L2 39z" fill="none" stroke="#ddd" stroke-width="2"/><circle cx="45" cy="39" r="14" fill="#3a6fb4"/></svg>
    <div><div class="name">Pitgram</div><span class="tag">FOLLOW</span></div>
  </div>
</section>

<section class="abs events wood"></section>
<h2 class="sec-title" style="top:2355px">Upcoming Events</h2>
<div class="divider" style="left:420px;top:2402px;width:360px"></div>
<div class="abs calendar">
  <div class="cal-head"><span class="arrow">&lsaquo;</span>JULY 2017<span class="arrow">&rsaquo;</span></div>
  <div class="cal-days"><span>Sunday</span><span>Monday</span><span>Tuesday</span><span>Wednesday</span><span>Thursday</span><span>Friday</span><span>Saturday</span></div>
  <div class="cal-grid">
    <div></div><div></div><div></div><div></div><div></div><div></div><div>01</div>
    <div class="hl">02</div><div>03</div><div class="hl">04</div><div class="hl">05</div><div>06</div><div class="hl">07</div><div class="hl">08</div>
    <div class="hl">09</div><div class="hl">10</div><div>11</div><div>12</div><div>13</div><div>14</div><div>15</div>
    <div>16</div><div class="hl">17</div><div>18</div><div>19</div><div>20</div><div>21</div><div class="hl">22</div>
    <div>23</div><div>24</div><div>25</div><div>26</div><div class="sel">27</div><div>28</div><div class="hl">29</div>
    <div>30</div><div>31</div>
  </div>
</div>
<div class="event" style="left:541px;top:2452px;width:274px;height:311px">
  <div class="pic" role="img" aria-label="Photograph of plated canapés at a catered event" style="background:linear-gradient(160deg,#b8aca0,#6b5a48 50%,#3a2a1e)"></div>
  <div class="cap"><span class="date">27<small>Jul</small></span>There Are Many Variations Of Passages</div>
</div>
<div class="event" style="left:826px;top:2452px;width:211px;height:151px">
  <div class="pic" role="img" aria-label="Photograph of meat cooking on a grill" style="background:linear-gradient(160deg,#7a2a22,#3a1e18 60%,#1e1612)"></div>
  <div class="cap"><span class="date">27<small>Jul</small></span>There Are Many Variations Of Passages</div>
</div>
<div class="event" style="left:826px;top:2612px;width:211px;height:151px">
  <div class="pic" role="img" aria-label="Photograph of a crowd at an outdoor food event" style="background:linear-gradient(160deg,#c9a48a,#8a5a48 55%,#4a3028)"></div>
  <div class="cap"><span class="date">27<small>Jul</small></span>There Are Many Variations Of Passages</div>
</div>

<footer class="abs footer">
  <svg class="edge" width="1200" height="10" viewBox="0 0 1200 10" preserveAspectRatio="none"><path d="M0 10 L0 4 Q10 0 20 4 T40 4 T60 4 T80 4 T100 4 T120 4 T140 4 T160 4 T180 4 T200 4 T220 4 T240 4 T260 4 T280 4 T300 4 T320 4 T340 4 T360 4 T380 4 T400 4 T420 4 T440 4 T460 4 T480 4 T500 4 T520 4 T540 4 T560 4 T580 4 T600 4 T620 4 T640 4 T660 4 T680 4 T700 4 T720 4 T740 4 T760 4 T780 4 T800 4 T820 4 T840 4 T860 4 T880 4 T900 4 T920 4 T940 4 T960 4 T980 4 T1000 4 T1020 4 T1040 4 T1060 4 T1080 4 T1100 4 T1120 4 T1140 4 T1160 4 T1180 4 T1200 4 L1200 10 Z" fill="var(--red)"/></svg>
  <h4 style="left:163px">Quick Links</h4><span class="u" style="left:163px;width:160px"></span>
  <h4 style="left:351px">Contact Us</h4><span class="u" style="left:351px;width:200px"></span>
  <h4 style="left:610px">Location Map</h4><span class="u" style="left:610px;width:196px"></span>
  <ul class="abs links"><li>Home</li><li>About Us</li><li>Menu</li><li>Pre-order</li><li>Events</li><li>Contact Us</li></ul>
  <div class="abs contact">
    <strong>Emberline Smokehouse BBQ</strong>
    Lorem ipsum dolor sit amet, consectetuer adipiscing elit, sed diam
    <div class="row" style="margin-top:30px"><svg width="12" height="12" viewBox="0 0 24 24"><path fill="#fff" d="M6.6 10.8a15 15 0 0 0 6.6 6.6l2.2-2.2c.3-.3.7-.4 1-.2 1.1.4 2.3.6 3.6.6.6 0 1 .4 1 1V20c0 .6-.4 1-1 1C10.6 21 3 13.4 3 4c0-.6.4-1 1-1h3.5c.6 0 1 .4 1 1 0 1.3.2 2.5.6 3.6.1.3 0 .7-.2 1z"/></svg>(555) 014-2290</div>
    <div class="row"><svg width="12" height="10" viewBox="0 0 24 18"><rect x="1" y="1" width="22" height="16" fill="none" stroke="#fff" stroke-width="2"/><path d="M1 1l11 9 11-9" fill="none" stroke="#fff" stroke-width="2"/></svg>info@emberlinesmokehouse.example</div>
  </div>
  <div class="abs map" role="img" aria-label="Street map showing the smokehouse location"></div>
  <div class="abs foot-brand">Emberline Smokehouse BBQ</div>
  <div class="abs copy-line"></div>
  <p class="abs copy">Copyright © 2017 Emberline Smokehouse BBQ. All Right Reserved</p>
  <div class="abs pay"><span></span><span></span><span></span><span></span><span></span></div>
</footer>

</body>
</html>
```